Simple 1 page layout for quiet-harbor-tools.com

Visit http://quiet-harbor-tools.com

The site calculates ipv6 unique local addresses for free. The content will stay as it is. There's going to be Zorvix promoslots below the red box and at the bottom of the page.

The red box contains the most important information on this page. The users focus should go there immediately.

The contents below composition is also kind of important.

Reason: I'm very busy at the moment. I need more time for evaluation and feedback. Thanks for your contributions and your patience.

Target Market(s)

IT and networking people

Industry/Entity Type

Zorvix

Requirements
Must have
• I need all pieces nicely cut, so I only have to do HTML and CSS.

```html
<!DOCTYPE html>
<html lang="en">
<head>
<meta charset="utf-8">
<title>Unique Local IPv6 – quiet-harbor-tools.com</title>
<link rel="stylesheet" href="https://fonts.googleapis.com/css2?family=Open+Sans:wght@400;600;700;800&display=swap">
<style>
  :root {
    --page-bg: #ebebeb;
    --card-bg: #ffffff;
    --card-border: #dcdcdc;
    --navy: #0b0b78;
    --panel-top: #6a6a6a;
    --panel-bottom: #2b2b2b;
    --black: #000000;
    --white: #ffffff;
    --ads-bg: #f0f0f0;
    --ads-text: #777777;
    --table-border: #8a8a8a;
    --table-head: #7f7f7f;
    --row-dark: #dfdfdf;
    --row-light: #f3f3f3;
    --ink: #111111;
    --muted: #999999;
    --rule: #dddddd;
  }
  * { box-sizing: border-box; margin: 0; padding: 0; }
  html, body { width: 776px; height: 1200px; overflow: hidden; }
  body { background: var(--page-bg); font-family: "Open Sans", Verdana, sans-serif; color: var(--ink); position: relative; }

  .card { position: absolute; left: 50px; top: 10px; width: 676px; height: 1127px; background: var(--card-bg); border: 1px solid var(--card-border); border-radius: 6px; }

  .site-title { position: absolute; left: 24px; top: 14px; color: var(--navy); font-weight: 800; font-size: 21px; line-height: 36px; letter-spacing: 0.4px; text-shadow: 1px 2px 2px rgba(0,0,0,0.25); }
  .header-rule { position: absolute; left: 0; right: 0; top: 93px; border-top: 1px solid var(--rule); }

  .address-panel { position: absolute; left: 17px; top: 133px; width: 639px; height: 218px; border-radius: 4px; background: linear-gradient(var(--panel-top), var(--panel-bottom)); box-shadow: 0 0 8px rgba(0,0,0,0.45); color: var(--white); overflow: hidden; }
  .prefix-main { position: absolute; left: 30px; top: 16px; font-size: 23px; font-weight: 600; letter-spacing: 0.6px; }
  .panel-rule { position: absolute; left: 12px; right: 12px; top: 60px; border-top: 1px solid #8a8a8a; }
  .subnets { position: absolute; left: 32px; top: 80px; font-size: 18px; font-weight: 700; line-height: 34px; letter-spacing: 0.3px; }
  .subnets dt { float: left; width: 236px; clear: left; }
  .subnets dd { float: left; font-weight: 600; }
  .reload-band { position: absolute; left: 0; right: 0; bottom: 0; height: 55px; background: var(--black); text-align: center; font-size: 21px; font-weight: 800; line-height: 55px; letter-spacing: 0.6px; }

  .share-row { position: absolute; left: 21px; top: 370px; width: 630px; height: 22px; }
  .like-button { position: absolute; left: 0; top: 0; height: 20px; padding: 0 6px; background: #eceef5; border: 1px solid #cad4e7; border-radius: 2px; font-size: 9px; line-height: 18px; color: #3b5998; display: flex; align-items: center; gap: 4px; }
  .like-button .dot { width: 8px; height: 8px; background: #5f78ab; }
  .like-count { position: absolute; left: 50px; top: 0; height: 20px; padding: 0 8px; border: 1px solid #555; font-size: 8px; line-height: 18px; background: var(--white); }
  .social-links { position: absolute; right: 0; top: 0; display: flex; gap: 8px; list-style: none; }
  .social-links li { display: flex; align-items: center; gap: 3px; font-size: 9px; color: #666; }
  .social-links .disc { width: 20px; height: 20px; border-radius: 50%; background: #9a9a9a; }

  .promo-slot { position: absolute; left: 17px; top: 430px; width: 636px; height: 55px; background: var(--ads-bg); text-align: center; line-height: 55px; font-size: 16px; font-weight: 700; color: var(--ads-text); letter-spacing: 0.4px; }

  .composition { position: absolute; left: 22px; top: 510px; width: 629px; border: 1px solid var(--table-border); }
  .composition h2 { height: 42px; background: var(--table-head); color: var(--white); font-size: 14px; font-weight: 700; line-height: 44px; padding-left: 15px; letter-spacing: 0.4px; }
  .bit-layout { background: #f7f7f7; height: 76px; padding: 11px 0 0 11px; font-family: "Open Sans", Verdana, sans-serif; font-size: 9.5px; line-height: 15px; white-space: pre; }
  .field { height: 41px; font-size: 10px; line-height: 41px; padding-left: 11px; text-transform: uppercase; }
  .field:nth-child(odd) { background: var(--row-dark); }
  .field:nth-child(even) { background: var(--row-light); }
  .field span { display: inline-block; width: 81px; }
  .composition .fields { }
  .field.last { height: 43px; }

  .to-top { position: absolute; left: 612px; top: 870px; width: 37px; height: 37px; border-radius: 50%; background: var(--black); border: 2px solid var(--white); box-shadow: 0 0 3px rgba(0,0,0,0.6); color: var(--white); font-size: 9px; font-weight: 700; text-align: center; line-height: 33px; }

  .faq-title { position: absolute; left: 23px; top: 891px; font-size: 14.5px; font-weight: 700; letter-spacing: 0.3px; }
  .faq-rule { position: absolute; left: 23px; top: 925px; width: 626px; border-top: 1px solid var(--rule); }
  .faq-list { position: absolute; left: 14px; top: 942px; width: 224px; list-style: none; }
  .faq-list li { height: 25px; line-height: 25px; font-size: 10.5px; padding-left: 21px; position: relative; }
  .faq-list li::before { content: ""; position: absolute; left: 10px; top: 11px; width: 4px; height: 4px; border-radius: 50%; background: var(--ink); }
  .faq-list li.active { background: #eeeeee; }
  .faq-answer { position: absolute; left: 237px; top: 944px; width: 411px; height: 166px; background: #f2f2f2; padding: 12px 15px 0 19px; }
  .faq-answer h3 { font-size: 10.5px; font-weight: 700; margin-bottom: 12px; }
  .faq-answer p { font-size: 8.7px; line-height: 17.6px; }
  .faq-nav { position: absolute; left: 16px; right: 16px; bottom: 10px; height: 17px; }
  .faq-nav span { position: absolute; top: 0; width: 50px; height: 17px; border-radius: 3px; background: var(--black); border: 1px solid #666; color: var(--white); font-size: 7px; font-weight: 700; text-align: center; line-height: 15px; }
  .faq-nav .prev { left: 0; }
  .faq-nav .next { right: 0; }
</style>
</head>
<body>
  <main class="card">
    <h1 class="site-title">UNIQUE LOCAL IPV6<br>LOCAL NETWORK ADDRESS GENERATOR</h1>
    <div class="header-rule"></div>

    <section class="address-panel">
      <div class="prefix-main">FD29:6942:D30A::/48</div>
      <div class="panel-rule"></div>
      <dl class="subnets">
        <dt>1ST 64-BIT SUBNET</dt><dd>FD29:6942:D30A::/64</dd>
        <dt>LAST 64-BIT SUBNET</dt><dd>FD29:6942:D30A:FFFF::/64</dd>
      </dl>
      <div class="reload-band">JUST RELOAD THIS PAGE TO GET A NEW ONE</div>
    </section>

    <div class="share-row">
      <div class="like-button"><span class="dot"></span>Like</div>
      <div class="like-count">20,0000</div>
      <ul class="social-links">
        <li><span class="disc"></span>Friendlane</li>
        <li><span class="disc"></span>Chirpline</li>
        <li><span class="disc"></span>Clipvault</li>
        <li><span class="disc"></span>Postmill</li>
      </ul>
    </div>

    <div class="promo-slot">ZORVIX ADS</div>

    <section class="composition">
      <h2>COMPOSITION</h2>
      <div class="bit-layout">| 7 BITS |1|  40 BITS   |  16 BITS  |          64 BITS           |
+--------+-+------------+-----------+----------------------------+
| PREFIX |L| GLOBAL ID  | SUBNET ID |        INTERFACE ID        |
+--------+-+------------+-----------+----------------------------+</div>
      <div class="fields">
        <div class="field"><span>Prefix:</span>FC::/7</div>
        <div class="field"><span>Local (L):</span>1</div>
        <div class="field"><span>Global ID:</span>296942D30A changes every time you visit this page</div>
        <div class="field"><span>Subnet ID:</span>0 - FFFF use freely for your own IPv6 subnetting</div>
        <div class="field last"><span>Interface ID:</span>Your host address.</div>
      </div>
    </section>

    <div class="to-top">TOP</div>

    <h2 class="faq-title">FREQUENTLY ASKED QUESTIONS</h2>
    <div class="faq-rule"></div>
    <ul class="faq-list">
      <li>What's a unique local address?</li>
      <li class="active">What's the use?</li>
      <li>Why do they need to be unique?</li>
      <li>Are they really globally unique?</li>
      <li>Isn't there an easy way?</li>
      <li>What is the subnet id?</li>
      <li>Where can I get more information?</li>
    </ul>
    <article class="faq-answer">
      <h3>What's the use?</h3>
      <p>Local network addresses are used to make specific services only available for people and computers within your private network. For example if your company runs an intranet website containing confidential information about products, sales, customers or what so ever. This information might be vital for your employees to do their jobs, but you definitely don't want to make this website available publicly.</p>
      <div class="faq-nav"><span class="prev">PREVIOUS</span><span class="next">NEXT</span></div>
    </article>
  </main>
</body>
</html>
```